Buchcover-Design für Liebesgedichte
Zielgruppe
Ich möchte meine Liebesgedichte veröffentlichen.
Zielgruppe sind Frauen, Verliebte, Unglücklich Verliebte, frisch Getrennte
Aufgabenstellung
Titel: Kein Morgen trägt so leise fort
Untertitel: Verse zum Atemholen für Suchende
Das von mir vorlegte Cover sollte die Liebe ausdrücken. Durch das liegende Herz und durch die schwarz-rote fliessende Farbgebung im Hintergrund wollte ich ausdrücken, dass die Liebe und der Tod nah verwandt sind. Die Gedichte tragen dazu bei, als Liebender zu überleben. Damit ist gemeint, dass Liebende sich auf den unvermeidbaren Schmerz und die Verletzbarkeit in der Liebe einlassen müssen, um nicht dem kitschigen Liebesbegriff der Medien zu verfallen. Deshalb ist mir auch der Untertitel so wichtig.
Es sind aber auch ganz andere Gestaltungen möglich. Ist nur ein laienhafter Versuch von mir gewesen, auszudrücken, was ich im Cover sagen möchte

```html
<!DOCTYPE html>
<html lang="de">
<head>
<meta charset="utf-8">
<title>Kein Morgen trägt so leise fort – Buchumschlag</title>
<link rel="stylesheet" href="https://fonts.googleapis.com/css2?family=Antonio:wght@200;300&family=Bebas+Neue&family=Pinyon+Script&display=swap">
<style>
  :root {
    --page: #ffffff;
    --cover: #050303;
    --rose: #d8a89b;
    --ember: #a4473a;
    --ash: #ece7e2;
    --smoke-deep: #3a130a;
    --smoke-mid: #6e2a14;
    --flame: #f2b761;
  }
  * { margin: 0; padding: 0; box-sizing: border-box; }
  html, body { width: 862px; height: 1200px; overflow: hidden; background: var(--page); }
  .canvas { position: relative; width: 862px; height: 1200px; }

  .wrap {
    position: absolute; left: 0; top: 290px;
    width: 862px; height: 621px;
    background: var(--cover); overflow: hidden;
  }

  .artwork { position: absolute; border-radius: 50%; }
  .artwork--back-smoke {
    left: 30px; top: 50px; width: 345px; height: 410px;
    background: radial-gradient(ellipse at 50% 45%, var(--smoke-mid) 0%, var(--smoke-deep) 45%, rgba(5,3,3,0) 72%);
    opacity: .85;
  }
  .artwork--burning-heart {
    left: 505px; top: 75px; width: 340px; height: 350px;
    background: radial-gradient(ellipse at 50% 48%, var(--flame) 0%, #c8692a 22%, var(--smoke-mid) 42%, var(--smoke-deep) 58%, rgba(5,3,3,0) 74%);
  }

  .blurb {
    position: absolute; left: 40px; top: 122px; width: 320px;
    font-family: "Antonio", sans-serif; font-weight: 200;
    font-size: 14.5px; line-height: 20.6px; letter-spacing: 2.2px;
    color: var(--rose); text-align: center;
  }

  .spine-text {
    position: absolute; writing-mode: vertical-rl; transform: rotate(180deg);
    font-family: "Antonio", sans-serif; font-weight: 200; color: var(--rose);
    white-space: nowrap;
  }
  .spine-text--subtitle { left: 412px; top: 8px; font-size: 10px; letter-spacing: 2.4px; line-height: 19px; text-align: right; height: 150px; text-transform: uppercase; }
  .spine-text--author { left: 446px; top: 436px; font-size: 17px; letter-spacing: 5px; height: 176px; text-align: center; text-transform: uppercase; }

  .title { font-family: "Bebas Neue", sans-serif; line-height: .95; }
  .title__line { display: block; white-space: nowrap; }
  .title__line--light { color: var(--ash); }
  .title__line--main { color: var(--ember); }
  .title__initial {
    font-family: "Pinyon Script", cursive; color: var(--ember);
    line-height: 0; margin-right: 6px;
  }

  .title--front { position: absolute; left: 530px; top: 448px; width: 300px; }
  .title--front .title__line--top { font-size: 27px; padding-left: 80px; }
  .title--front .title__line--main { font-size: 46px; }
  .title--front .title__line--end { font-size: 27px; padding-left: 100px; }
  .title--front .title__initial { font-size: 64px; vertical-align: -6px; }

  .title--spine {
    position: absolute; left: 404px; top: 402px; width: 200px;
    transform-origin: 0 0; transform: rotate(-90deg);
  }
  .title--spine .title__line--top { font-size: 17px; padding-left: 50px; }
  .title--spine .title__line--main { font-size: 29px; }
  .title--spine .title__line--end { font-size: 17px; padding-left: 62px; }
  .title--spine .title__initial { font-size: 40px; vertical-align: -4px; margin-right: 4px; }

  .author {
    position: absolute; left: 530px; top: 30px; width: 290px; text-align: center;
    font-family: "Antonio", sans-serif; font-weight: 200; white-space: nowrap;
    font-size: 24px; letter-spacing: 6px; color: var(--rose); text-transform: uppercase;
  }

  .subtitle {
    position: absolute; left: 500px; top: 574px; width: 360px; text-align: center;
    font-family: "Antonio", sans-serif; font-weight: 200; white-space: nowrap;
    font-size: 16px; letter-spacing: 3.6px; color: var(--rose);
  }
</style>
</head>
<body>
<div class="canvas">
  <section class="wrap" aria-label="Buchumschlag, ausgebreitet">
    <!-- Rückseite -->
    <div class="artwork artwork--back-smoke" role="img" aria-label="Dunkelroter, fließender Rauch auf Schwarz"></div>
    <p class="blurb">Lorem ipsum<br>dolor sit amet,<br>consectetur adipiscing<br>elit, sed do eiusmod<br>tempor incididunt ut labore<br>et dolore magna aliqua. Quis<br>ipsum suspendisse ultrices<br>gravida. Risus commodo<br>viverra maecenas accumsan<br>lacus vel facilisis. Lorem<br>ipsum dolor sit amet,<br>consectetur adipiscing<br>elit, sed do<br>eiusmod.</p>

    <!-- Buchrücken -->
    <p class="spine-text spine-text--subtitle">Verse zum Atemholen<br>für Suchende</p>
    <h2 class="title title--spine">
      <span class="title__line title__line--light title__line--top">Kein Morgen</span>
      <span class="title__line title__line--main"><span class="title__initial">T</span>rägt so leise</span>
      <span class="title__line title__line--light title__line--end">fort</span>
    </h2>
    <p class="spine-text spine-text--author">Tobias Werhahn</p>

    <!-- Vorderseite -->
    <p class="author">Tobias Werhahn</p>
    <div class="artwork artwork--burning-heart" role="img" aria-label="Liegendes, brennendes Herz in rotem Rauch"></div>
    <h1 class="title title--front">
      <span class="title__line title__line--light title__line--top">Kein Morgen</span>
      <span class="title__line title__line--main"><span class="title__initial">T</span>rägt so leise</span>
      <span class="title__line title__line--light title__line--end">fort</span>
    </h1>
    <p class="subtitle">VERSE ZUM ATEMHOLEN FÜR SUCHENDE</p>
  </section>
</div>
</body>
</html>
```